Time for a new business card design

We need a new business card design for Tolvik Furniture Rentals based in Australia. www.tolvik-example.com.au. We specialise in providing furniture rentals for home staging, corporate relocations events and product launches etc. We would like to see designs that include our logo on the front of the card with all the standard contact details as well as having a realy nice image on the back with a list of our services we offer. Our logo is red and this cannot change. Were looking for a pallet of red and white with maybe a splash of grey. The final design should communication organised & stylish. We are in the process of finalising our new website and would like the card design to compliment this as well

Requirements
Must have
• Square corners
logo
name, title, email, phone, address
image on back of card with space for list of services we offer
Services:
•Furniture and appliance rental
•Property styling
•Events and functions
•Office furniture rental

The card must be landscape.
The image is to appear on the back of the card only.

```html
<!DOCTYPE html>
<html lang="en">
<head>
<meta charset="utf-8">
<title>Tolvik Furniture Rentals – Business Card</title>
<link rel="stylesheet" href="https://fonts.googleapis.com/css2?family=Arimo:wght@400;700&display=swap">
<style>
  :root {
    --red: #b5121b;
    --light-grey: #e6e6e8;
    --white: #ffffff;
    --page: #ffffff;
    --photo-dark: #3a3a3a;
    --photo-mid: #8a8a8a;
    --photo-light: #d2d2d2;
  }
  * { margin: 0; padding: 0; box-sizing: border-box; }
  html, body {
    width: 1064px; height: 1200px; overflow: hidden;
    background: var(--page);
    font-family: "Arimo", Arial, sans-serif;
  }
  .card {
    position: absolute; left: 141px; width: 771px; height: 442px;
    overflow: hidden;
  }
  .card-front { top: 125px; }
  .card-back { top: 636px; }

  .front-header {
    position: absolute; left: 0; top: 0; width: 100%; height: 186px;
    background: var(--light-grey);
  }
  .brand-name {
    position: absolute; left: 36px; top: 70px;
    font-size: 64px; font-weight: 400; color: var(--red);
    letter-spacing: -1px; white-space: nowrap;
  }
  .front-body {
    position: absolute; left: 0; top: 186px; width: 100%; height: 256px;
    background: var(--red); color: var(--white);
  }
  .person {
    position: absolute; left: 60px; top: 94px; width: 344px;
    text-align: center;
  }
  .person-name { font-size: 27px; font-weight: 700; line-height: 32px; }
  .person-title { font-size: 24px; line-height: 30px; }
  .contact {
    position: absolute; left: 404px; top: 52px;
    font-size: 25px; line-height: 30px;
  }
  .address { margin-bottom: 8px; }
  .contact-row { display: flex; align-items: center; gap: 8px; line-height: 30px; }
  .contact-row svg { width: 20px; height: 20px; fill: var(--white); flex: none; }

  .back-photo {
    position: absolute; inset: 0;
    background:
      radial-gradient(ellipse at 30% 75%, var(--photo-light) 0%, var(--photo-mid) 45%, transparent 70%),
      linear-gradient(160deg, var(--photo-dark) 0%, var(--photo-mid) 45%, var(--photo-light) 70%, var(--photo-mid) 100%);
  }
  .back-brand {
    position: absolute; left: 40px; top: 50px;
    font-size: 40px; font-weight: 400; color: var(--white);
    letter-spacing: -0.5px; white-space: nowrap;
  }
  .services {
    position: absolute; left: 425px; top: 278px;
    color: var(--white); font-size: 21px; line-height: 26px;
  }
  .services-title { font-weight: 700; padding-left: 16px; }
  .services-list { list-style: none; }
  .services-list li { position: relative; padding-left: 16px; }
  .services-list li::before {
    content: ""; position: absolute; left: -10px; top: 5px;
    width: 16px; height: 16px; background: var(--red);
  }
</style>
</head>
<body>
  <section class="card card-front" aria-label="Card front">
    <header class="front-header">
      <div class="brand-name">Tolvik Furniture Rentals</div>
    </header>
    <div class="front-body">
      <div class="person">
        <div class="person-name">Your Name</div>
        <div class="person-title">Your Title</div>
      </div>
      <div class="contact">
        <div class="address">18 Harbourline Lane<br>Marlow NSW 2199</div>
        <div class="contact-row">
          <svg viewBox="0 0 24 24" aria-hidden="true"><path d="M3 8c0-3 4-5 9-5s9 2 9 5v2h-5V7.5c-1.2-.5-2.5-.7-4-.7s-2.8.2-4 .7V10H3z"/></svg>
          <span>02 9000 1482</span>
        </div>
        <div class="contact-row">
          <svg viewBox="0 0 24 24" aria-hidden="true"><path d="M6 2h10v6H6zM3 9h18v12H3zm3 3v2h3v-2zm5 0v2h3v-2zm-5 4v2h3v-2zm5 0v2h3v-2z"/></svg>
          <span>02 9000 1483</span>
        </div>
        <div class="contact-row">
          <svg viewBox="0 0 24 24" aria-hidden="true"><path d="M2 5h20v14H2zm2 2v.5l8 5.5 8-5.5V7l-8 5z"/></svg>
          <span>email@tolvik-example.com.au</span>
        </div>
      </div>
    </div>
  </section>

  <section class="card card-back" aria-label="Card back">
    <div class="back-photo" role="img" aria-label="Black and white photo of a styled bedroom with cushions, a lamp and stacked books"></div>
    <div class="back-brand">Tolvik Furniture Rentals</div>
    <div class="services">
      <div class="services-title">Services:</div>
      <ul class="services-list">
        <li>Furniture and appliance rental</li>
        <li>Property styling</li>
        <li>Events and functions</li>
        <li>Office furniture rental</li>
      </ul>
    </div>
  </section>
</body>
</html>
```